Design graphics and Print for a line of Herb Seeds- Envelope Design

We need a set of herb seed envelopes designed for a new seed line we are launching.
The design will be both front and back

Envelope will be a colored ( green) ) envelope with white text
or a white or cream envelope in all black /and images text. Or can add some colors to the white envelope.

I have attached the die-cut of the seed envelope.
I have attached some images of envelopes I like. Please do not copy, these are just to give you an idea of what I like.

Please feel free to reach out to me if you have any questions.

Thank you

Target Market(s)

The design needs to classic that can translate to 3 different audiences. 1. young parents 2. hip, young single millennial 3. kids

Industry/Entity Type

Ecommerce

Font styles to use
Serif

Requirements
Must have
• Please use the herb - Parsley for the design
Icon, Text or both.

Front side must have:
1.either herb Icon or work Parsley or both- this will be the main attraction
2. company name- Tall Meadow Pantry
3. can use design elements
4. can use my logo on from or back or not at all. I

Backside must have:
1. social media tags
FB, Photogram and Pinboardy ( use icons) @tallmeadowpantry

my website: www.tallmeadowpantry.example
this can be on from or back of the envelope.
Should not have
• please stay away from "county" flowery, old fashioned style designs

```html
<!DOCTYPE html>
<html lang="en">
<head>
<meta charset="utf-8">
<title>Tall Meadow Pantry – Parsley Seed Envelope</title>
<link rel="stylesheet" href="https://fonts.googleapis.com/css2?family=Montserrat:wght@400;500;600;700&family=Playfair+Display:wght@700&display=swap">
<style>
  :root {
    --leaf-green: #2c6410;
    --deep-green: #173a1c;
    --pale-sage: #d4dcc6;
    --soft-leaf: #6d9a55;
    --herb-light: #7fb236;
    --herb-mid: #4f8f22;
    --herb-dark: #2f6a14;
    --ink: #1e3325;
    --paper: #ffffff;
    --die-line: #3a3a3a;
    --seal-line: #3b3b36;
    --tag-pin: #cb2027;
    --tag-photo: #b5338c;
    --tag-video: #e62117;
    --tag-friend: #3b5998;
  }
  * { box-sizing: border-box; margin: 0; padding: 0; }
  html, body { width: 1200px; height: 1000px; overflow: hidden; background: var(--paper); }
  .canvas { position: relative; width: 1200px; height: 1000px; background: var(--paper); font-family: "Montserrat", Arial, sans-serif; }

  /* Back panel */
  .back-panel { position: absolute; left: 104px; top: 172px; width: 497px; height: 688px; border: 1px solid var(--die-line); background: var(--paper); overflow: hidden; }
  .back-panel__field { position: absolute; left: 0; top: 0; width: 100%; height: 496px; background: var(--leaf-green); }
  .back-panel__sprig { position: absolute; left: 0; top: 0; width: 218px; height: 216px; border-radius: 0 0 100% 0; background: linear-gradient(135deg, rgba(120,165,95,0.55), rgba(109,154,85,0.35)); }
  .back-panel__tagline { position: absolute; top: 50px; width: 100%; text-align: center; color: #eef2e8; font-weight: 600; font-size: 29px; }
  .back-panel__brand { position: absolute; top: 374px; width: 100%; text-align: center; font-family: "Playfair Display", Georgia, serif; font-weight: 700; color: var(--pale-sage); }
  .back-panel__brand-main { display: block; font-size: 34px; line-height: 1.1; }
  .back-panel__brand-sub { display: block; font-size: 23px; line-height: 1.2; }
  .back-panel__seal { position: absolute; left: 214px; top: 456px; width: 82px; height: 82px; border-radius: 50%; background: var(--paper); border: 3px solid var(--seal-line); }
  .social-list { position: absolute; top: 564px; left: 124px; display: grid; grid-template-columns: 146px 140px; row-gap: 4px; list-style: none; }
  .social-list__item { display: flex; align-items: center; gap: 16px; font-size: 18px; color: var(--ink); }
  .social-list__icon { width: 17px; height: 17px; border-radius: 50%; flex: none; }
  .social-list__icon--pin { background: var(--tag-pin); }
  .social-list__icon--photo { background: var(--tag-photo); }
  .social-list__icon--video { background: var(--tag-video); }
  .social-list__icon--friend { background: var(--tag-friend); }
  .back-panel__web { position: absolute; top: 618px; width: 100%; text-align: center; font-size: 20px; color: var(--ink); }
  .back-panel__handle { position: absolute; top: 650px; width: 100%; text-align: center; font-size: 15px; color: var(--ink); }

  /* Front panel */
  .front-flap { position: absolute; left: 598px; top: 102px; width: 499px; height: 71px; background: var(--leaf-green); border-radius: 40px 40px 0 0; }
  .front-panel { position: absolute; left: 600px; top: 172px; width: 497px; height: 688px; border: 1px solid var(--die-line); background: var(--paper); }
  .front-panel__header { position: absolute; top: 21px; width: 100%; display: flex; justify-content: center; align-items: center; gap: 10px; font-family: "Playfair Display", Georgia, serif; font-weight: 700; font-size: 20px; color: var(--deep-green); }
  .front-panel__header-mark { width: 44px; height: 44px; border-radius: 50%; border: 2px solid var(--deep-green); }
  .front-panel__band { position: absolute; top: 82px; left: 0; width: 100%; height: 96px; background: var(--leaf-green); display: flex; align-items: center; justify-content: center; }
  .front-panel__title { color: var(--paper); font-weight: 700; font-size: 44px; letter-spacing: 0.5px; }
  .front-panel__herb { position: absolute; left: 72px; top: 240px; width: 350px; height: 372px; border-radius: 28px; background: linear-gradient(160deg, var(--herb-light) 0%, var(--herb-mid) 50%, var(--herb-dark) 100%); }
  .front-panel__web { position: absolute; top: 643px; width: 100%; text-align: center; font-size: 20px; color: var(--ink); }
</style>
</head>
<body>
<main class="canvas">
  <section class="back-panel">
    <div class="back-panel__field">
      <div class="back-panel__sprig" role="img" aria-label="Faint parsley sprig decoration"></div>
      <p class="back-panel__tagline">Grow your Own!</p>
      <p class="back-panel__brand">
        <span class="back-panel__brand-main">Tall Meadow</span>
        <span class="back-panel__brand-sub">Pantry</span>
      </p>
    </div>
    <div class="back-panel__seal"></div>
    <ul class="social-list">
      <li class="social-list__item"><span class="social-list__icon social-list__icon--pin"></span>Pinboardy</li>
      <li class="social-list__item"><span class="social-list__icon social-list__icon--photo"></span>Photogram</li>
      <li class="social-list__item"><span class="social-list__icon social-list__icon--video"></span>Vidstream</li>
      <li class="social-list__item"><span class="social-list__icon social-list__icon--friend"></span>Friendbook</li>
    </ul>
    <p class="back-panel__web">www.tallmeadowpantry.example</p>
    <p class="back-panel__handle">@tallmeadowpantry</p>
  </section>

  <div class="front-flap"></div>
  <section class="front-panel">
    <div class="front-panel__header">
      <span>Tall Meadow Pantry</span>
      <span class="front-panel__header-mark"></span>
    </div>
    <div class="front-panel__band"><h1 class="front-panel__title">PARSLEY</h1></div>
    <div class="front-panel__herb" role="img" aria-label="Illustration of a fresh green parsley sprig"></div>
    <p class="front-panel__web">www.tallmeadowpantry.example</p>
  </section>
</main>
</body>
</html>
```